I need a shopify website for a beauty brand that i am starting. The name of the brand is called "Velna Beauty" i need the website to have a "Sleek Sexy And Mordern Design" preferable with a "Black Colour Scheme" i need the shopify store to be "Integrated With Instagram and Facebook" (@VelnaBeauty on Instagram and Velna Beauty On Facebook) ... I Also need to be able to "Easily to upload future products" (as ive only got three products at the moment) and i will also need to be "Able to capture emails to use for email marketing in the future as the brand grows "

```html
<!DOCTYPE html>
<html lang="en">
<head>
<meta charset="utf-8">
<title>Velna Beauty</title>
<link href="https://fonts.googleapis.com/css2?family=Arimo:wght@400;700&family=Crimson+Pro:wght@400;500;600&display=swap" rel="stylesheet">
<style>
:root{
  --black:#000;
  --ink:#111;
  --white:#fff;
  --pink:#f0676d;
  --grey-bg:#f1f1f1;
  --muted:#333;
  --serif:"Crimson Pro", Georgia, serif;
  --sans:"Arimo", Arial, sans-serif;
}
*{box-sizing:border-box;margin:0;padding:0}
html,body{width:1200px;height:4197px;overflow:hidden;background:var(--black)}
body{position:relative;font-family:var(--sans);color:var(--white)}
.abs{position:absolute}
.center{text-align:center}

/* header */
.site-header{left:0;top:0;width:1200px;height:121px;background:var(--black)}
.brand{left:111px;top:28px;font-family:var(--serif);font-size:26px;font-weight:500;letter-spacing:3px;color:var(--white)}
.brand small{display:block;font-size:14px;letter-spacing:4px;margin-top:2px}
.header-icons{right:111px;top:26px;display:flex;gap:14px}
.main-nav{right:111px;top:80px;display:flex;gap:42px;font-size:12px;font-weight:700;letter-spacing:.3px}
.main-nav .active{color:var(--pink)}
.caret{display:inline-block;border:4px solid transparent;border-top:5px solid var(--white);margin-left:3px;vertical-align:-1px}

/* hero */
.hero{left:0;top:121px;width:1200px;height:523px;background:radial-gradient(ellipse at 62% 60%,#4a3830 0%,#2b1f1a 45%,#140d0a 100%)}
.hero-title{left:111px;top:274px;font-family:var(--serif);font-size:46px;font-weight:500;color:var(--pink);letter-spacing:1px}
.hero-text{left:111px;top:336px;width:441px;font-size:12px;font-weight:700;line-height:20px;text-align:justify}
.btn{display:flex;align-items:center;justify-content:center;font-size:12px;font-weight:700;background:var(--white);color:var(--ink);letter-spacing:.3px}
.btn-dark{background:var(--ink);color:var(--white)}
.hero-dots{left:546px;top:619px;display:flex;gap:9px}
.hero-dots i{width:19px;height:4px;background:var(--white)}
.hero-dots i.on{background:var(--pink)}

/* sections */
.section-title{left:0;width:1200px;font-family:var(--serif);font-size:34px;font-weight:500}
.section-text{left:260px;width:680px;font-size:12px;line-height:21px}

/* collection cards */
.card{background:var(--white);color:var(--ink)}
.card .ph{position:absolute;left:20%;top:8%;width:60%;height:50%;background:radial-gradient(ellipse at center,#d9d9d9 0%,#f4f4f4 60%,#fff 100%)}
.card h3{position:absolute;left:0;width:100%;top:290px;font-family:var(--serif);font-size:27px;font-weight:500;text-align:center}
.card p{position:absolute;left:0;width:100%;top:332px;font-size:12px;text-align:center;color:var(--muted)}

.banner{left:0;top:1864px;width:1200px;height:326px;background:linear-gradient(90deg,#0d121b,#141b26 50%,#0d121b)}
.banner-photo{left:484px;top:1864px;width:253px;height:326px;background:linear-gradient(180deg,#6d4b3c,#b98470 45%,#1a1a1a 85%)}

/* featured products */
.product{background:var(--white);color:var(--ink)}
.sale{position:absolute;left:8px;top:10px;width:64px;height:29px;background:var(--pink);color:var(--white);font-size:11px;font-weight:700;display:flex;align-items:center;justify-content:center}
.product .ph{position:absolute;left:20px;top:50px;width:188px;height:110px;background:radial-gradient(ellipse at center,#cfcfcf 0%,#f3f3f3 55%,#fff 100%)}
.product h4{position:absolute;left:13px;top:200px;font-family:var(--serif);font-size:22px;font-weight:400}
.product .price{position:absolute;left:13px;top:232px;font-family:var(--serif);font-size:22px;color:var(--pink)}
.promo{background:linear-gradient(160deg,#5a3a2e,#2b1c16 55%,#4a352c)}
.promo h4{position:absolute;left:0;width:100%;top:122px;text-align:center;font-family:var(--serif);font-size:22px;color:var(--pink)}
.promo p{position:absolute;left:14px;right:14px;top:153px;text-align:center;font-size:8px;line-height:12px;font-weight:700}
.promo .field{position:absolute;left:20px;top:200px;width:128px;height:26px;background:var(--white);color:#888;font-size:9px;font-style:italic;padding:8px 10px}
.promo .go{position:absolute;left:148px;top:200px;width:62px;height:26px;background:var(--pink);font-family:var(--serif);font-size:12px;font-weight:600;display:flex;align-items:center;justify-content:center}

.story-photo{background:linear-gradient(180deg,#8a6c5e,#c79f8c 40%,#7d5a4c 75%,#a07c6c)}
.story-title{font-family:var(--serif);font-size:27px;font-weight:500}
.story-sub{font-size:16px;font-weight:700}
.story-text{font-size:12px;line-height:20px}

/* news */
.news{left:0;top:3344px;width:1200px;height:391px;background:var(--grey-bg);color:var(--ink)}
.news-photo{left:598px;top:3456px;width:491px;height:235px;background:linear-gradient(180deg,#a0786a,#d3ae9c 45%,#b48c7b);border:1px solid #bbb}

/* footer */
.footer{left:0;top:3735px;width:1200px;height:462px;background:var(--black)}
.foot-h{font-family:var(--serif);font-size:17px;font-weight:500}
.foot-t{font-size:12px}
.socials{left:111px;top:3957px;display:flex;gap:6px}
.socials i{width:41px;height:41px;border:2px solid var(--white);border-radius:50%}
.store-badge{width:135px;height:39px;border:1.5px solid #aaa;border-radius:7px;background:var(--black)}
.foot-links{left:453px;top:3919px;font-size:12px;font-weight:700;line-height:22px}
.subscribe{left:703px;top:3954px;width:386px;height:40px;background:var(--white);color:var(--ink);font-size:12px;font-weight:700;display:flex;align-items:center;justify-content:flex-end;padding-right:20px}
.copyright{left:0;top:4155px;width:1200px;font-size:12px;color:#ccc}
</style>
</head>
<body>

<header class="abs site-header">
  <div class="abs brand">VELNA<small>VELNA BEAUTY</small></div>
  <div class="abs header-icons">
    <svg width="18" height="18" viewBox="0 0 18 18"><circle cx="7.5" cy="7.5" r="5.5" fill="none" stroke="#fff" stroke-width="2.5"/><line x1="11.5" y1="11.5" x2="16.5" y2="16.5" stroke="#fff" stroke-width="3" stroke-linecap="round"/></svg>
    <svg width="16" height="18" viewBox="0 0 16 18"><circle cx="8" cy="5" r="4.5" fill="#fff"/><path d="M0 18c0-6 3-8 8-8s8 2 8 8z" fill="#fff"/></svg>
    <svg width="20" height="18" viewBox="0 0 20 18"><path d="M0 1h3.5l2.5 10h11l2-7H5" fill="none" stroke="#fff" stroke-width="2"/><path d="M5 4h14l-2 7H6z" fill="#fff"/><circle cx="7.5" cy="15.5" r="2" fill="#fff"/><circle cx="15.5" cy="15.5" r="2" fill="#fff"/></svg>
  </div>
  <nav class="abs main-nav">
    <span class="active">HOME</span>
    <span>STORE<i class="caret"></i></span>
    <span>SERVICE</span>
    <span>ABOUT</span>
    <span>BLOG<i class="caret"></i></span>
    <span>CONTACT</span>
  </nav>
</header>

<section class="abs hero" role="img" aria-label="Close-up photograph of an eye with long dark lashes"></section>
<h1 class="abs hero-title">VELNA BEAUTY</h1>
<p class="abs hero-text">There are many variations of passages of Lorem Ipsum available, but the majority have suffered alteration in some form, by injected humour, or randomised words which don't look even slightly believable. If you are going to use a passage of Lorem Ipsum.</p>
<a class="abs btn" style="left:111px;top:434px;width:134px;height:45px">LEARN MORE</a>
<div class="abs hero-dots"><i></i><i></i><i class="on"></i><i></i></div>

<h2 class="abs section-title center" style="top:702px">Collection Of Velna Beauty</h2>
<p class="abs section-text center" style="top:766px">There are many variations of passages of Lorem Ipsum available, but the majority have suffered alteration in some form, by injected humour, or randomised words which don't look even slightly believable.</p>
<a class="abs btn" style="left:533px;top:823px;width:134px;height:44px">SHOP NOW !</a>

<article class="abs card" style="left:111px;top:941px;width:455px;height:399px"><div class="ph" role="img" aria-label="Pair of false eyelashes"></div><h3>Simply Dummy Text</h3><p>There are many variations of passages of Lorem Ipsum</p></article>
<article class="abs card" style="left:633px;top:941px;width:455px;height:399px"><div class="ph" role="img" aria-label="Pair of false eyelashes"></div><h3>Simply Dummy Text</h3><p>There are many variations of passages of Lorem Ipsum</p></article>
<article class="abs card" style="left:111px;top:1394px;width:455px;height:401px"><div class="ph" role="img" aria-label="Pair of false eyelashes"></div><h3>Simply Dummy Text</h3><p>There are many variations of passages of Lorem Ipsum</p></article>
<article class="abs card" style="left:633px;top:1394px;width:455px;height:401px"><div class="ph" role="img" aria-label="Pair of false eyelashes"></div><h3>Simply Dummy Text</h3><p>There are many variations of passages of Lorem Ipsum</p></article>

<div class="abs banner"></div>
<div class="abs banner-photo" role="img" aria-label="Portrait photograph of a model wearing lashes and a black top"></div>

<h2 class="abs section-title center" style="top:2222px">Featured Collection</h2>
<p class="abs section-text center" style="top:2286px">There are many variations of passages of Lorem Ipsum available, but the majority have suffered alteration in some form, by injected humour, or randomised words which don't look even slightly believable.</p>
<a class="abs btn" style="left:533px;top:2341px;width:134px;height:44px">VIEW MORE</a>

<article class="abs product" style="left:111px;top:2431px;width:228px;height:274px"><span class="sale">SALE</span><div class="ph" role="img" aria-label="Pair of false eyelashes"></div><h4>Dummy text</h4><span class="price">$ 18.00</span></article>
<article class="abs product" style="left:360px;top:2431px;width:229px;height:274px"><span class="sale">SALE</span><div class="ph" role="img" aria-label="Pair of false eyelashes"></div><h4>Dummy text</h4><span class="price">$ 15.00</span></article>
<article class="abs product" style="left:610px;top:2431px;width:228px;height:274px"><span class="sale">SALE</span><div class="ph" role="img" aria-label="Pair of false eyelashes"></div><h4>Dummy text</h4><span class="price">$ 17.00</span></article>
<aside class="abs promo" style="left:859px;top:2431px;width:228px;height:274px" role="img" aria-label="Close-up photograph of lashes behind an email offer">
  <h4>Today Only</h4>
  <p>There are many variations of passages of Lorem Ipsum available, but the majority have.</p>
  <div class="field">Your Email</div>
  <div class="go">Sign In</div>
</aside>

<div class="abs story-photo" style="left:111px;top:2757px;width:479px;height:256px" role="img" aria-label="Photograph of eyes with smoky makeup and lashes"></div>
<div class="abs center" style="left:606px;top:2786px;width:458px">
  <h3 class="story-title">Simply Dummy Text of</h3>
  <p class="story-sub" style="margin-top:8px">Lorem Ipsum</p>
  <p class="story-text" style="margin-top:12px">There are many variations of passages of Lorem Ipsum available, but the majority have suffered alteration</p>
</div>
<a class="abs btn" style="left:768px;top:2930px;width:134px;height:45px">OUR STORY</a>

<div class="abs center" style="left:111px;top:3067px;width:457px">
  <h3 class="story-title">Simply Dummy Text of</h3>
  <p class="story-sub" style="margin-top:8px">Lorem Ipsum</p>
  <p class="story-text" style="margin-top:12px">There are many variations of passages of Lorem Ipsum available, but the majority have suffered alteration</p>
</div>
<a class="abs btn" style="left:274px;top:3212px;width:132px;height:44px">OUR STORY</a>
<div class="abs story-photo" style="left:606px;top:3039px;width:480px;height:254px" role="img" aria-label="Photograph of closed eyes wearing long lashes"></div>

<section class="abs news">
  <h2 class="abs section-title center" style="top:34px;color:var(--ink)">Latest news</h2>
  <h3 class="abs" style="left:111px;top:111px;font-family:var(--serif);font-size:25px;font-weight:500">We're Live</h3>
  <p class="abs" style="left:111px;top:147px;font-size:12px;font-weight:700">Posted by Social Media Lead</p>
  <p class="abs" style="left:111px;top:171px;font-size:12px;font-weight:700">MARCH 24, 2020</p>
  <p class="abs" style="left:111px;top:207px;width:400px;font-size:12px;line-height:22px">There are many variations of passages of Lorem Ipsum available, but the majority have suffered alteration in some form, by injected humour, or randomised words which.</p>
  <a class="abs btn btn-dark" style="left:111px;top:293px;width:134px;height:44px">VIEW MORE</a>
</section>
<div class="abs news-photo" role="img" aria-label="Photograph of closed eyes with long lashes"></div>

<footer class="abs footer"></footer>
<div class="abs brand" style="top:3803px">VELNA<small>VELNA BEAUTY</small></div>
<h4 class="abs foot-h" style="left:111px;top:3890px">Follow Us</h4>
<p class="abs foot-t" style="left:111px;top:3920px">There are many variations of passages</p>
<div class="abs socials"><i></i><i></i><i></i><i></i><i></i></div>
<h4 class="abs foot-h" style="left:111px;top:4021px">Follow Us</h4>
<div class="abs store-badge" style="left:111px;top:4060px" role="img" aria-label="Mobile app store badge"></div>
<div class="abs store-badge" style="left:111px;top:4107px" role="img" aria-label="Mobile app store badge"></div>

<h4 class="abs foot-h" style="left:453px;top:3890px">Follow Us</h4>
<div class="abs foot-links">Home<br>Store<br>Service<br>About<br>Blog<br>Contact</div>

<h4 class="abs foot-h" style="left:703px;top:3890px">Introduce an email offer</h4>
<p class="abs foot-t" style="left:703px;top:3920px">Entice shoppers to sign up for your list</p>
<div class="abs subscribe">SUBSCRIBE</div>

<p class="abs copyright center">copyright@ 2021 Velna Beauty all rights reserved</p>

</body>
</html>
```